Bday & 7th year in Singapore

I'll be celebrating my thirty something birthday and 7th year in Singapore on Sat 29 June 2013, 830pm til late. Still looking for a venue so please leave some space for it and the address so it can be added.
Required:
Sat, 29 June
830pm
Venue TBC
I would like the poster to have an "infographic" look and feel, ideally with blue, grey, and red tones.
I would like invitees to feel that it's going to a great night of live music, drinks and mingling with existing and new friends so it would be awesome if they can be there.
I love traveling, clubbing, going on food adventures, singing.
People need to know that it's primarily a bday party (main design element) but that I'm also celebrating my 7th year in Singapore.
I'm looking for the most creative design so people will get excited and book their diaries as soon as they see the invitation.
Output required: high quality JPEG I can post on Pindlebox event page and also something I can use for A3 printing. Winning designer should be able to accommodate a revision on venue after decision is made as I can only confirm venue after the deadline.
Reason: Extended the deadline as I realise 2 days is quite tight given nature of the project.
Reason: Waiting for venue to be confirmed so it can be built into the poster
Target Market(s)
Invitees would be between 23 and 35 years old so should appeal to them
Industry/Entity Type
Printing
Requirements
Must have
- Singapore famous landmarks like Corlow Quay Towers, Singapore skyline, Verandine, Tidecrest, but they should not be the centre of attraction
Nice to have
- My photo (attached) but drawn in a nice way

```html
<!DOCTYPE html>
<html lang="en">
<head>
<meta charset="utf-8">
<title>30th Birthday &amp; 7th Year in Singapore — Invitation</title>
<link rel="stylesheet" href="https://fonts.googleapis.com/css2?family=Alfa+Slab+One&family=Cormorant+Garamond:ital,wght@1,500&family=Josefin+Sans:wght@400&family=Playfair+Display:ital,wght@1,400;1,700&family=Righteous&family=Rubik:wght@900&display=swap">
<style>
  :root {
    --frame: #8a8a8a;
    --sky-blue: #4a8fc1;
    --steel-blue: #3f7ea8;
    --pale: #e9ecec;
    --sun-yellow: #fde03c;
    --slate: #6e6768;
    --shadow-violet: #7f7a9c;
    --flag-red: #f04a35;
  }
  html, body {
    margin: 0;
    padding: 0;
    width: 900px;
    height: 1200px;
    overflow: hidden;
    background: #ffffff;
  }
  .invitation {
    position: relative;
    width: 900px;
    height: 1200px;
    background: var(--frame);
    overflow: hidden;
  }
  .invitation__panel {
    position: absolute;
    left: 28px;
    top: 36px;
    width: 844px;
    height: 1128px;
    overflow: hidden;
    background:
      radial-gradient(ellipse 420px 260px at 30% 18%, rgba(64,132,190,0.95), rgba(64,132,190,0) 100%),
      linear-gradient(180deg, #5b9acb 0%, #9cc0da 30%, #d8e2e8 52%, #eceeee 70%, #e2e4e4 100%);
  }
  .line { position: absolute; margin: 0; white-space: nowrap; line-height: 1; }

  .line--you {
    left: 42px; top: 20px;
    font-family: "Rubik", sans-serif; font-weight: 900;
    font-size: 190px; letter-spacing: -4px;
    color: var(--sun-yellow);
    text-shadow: -6px 5px 0 var(--shadow-violet);
  }
  .line--are, .line--invited {
    font-family: "Righteous", sans-serif;
    color: var(--steel-blue);
    text-shadow: -4px 4px 0 var(--sun-yellow);
  }
  .line--are { left: 478px; top: 10px; font-size: 112px; }
  .line--invited { left: 478px; top: 92px; font-size: 96px; }

  .line--to-my {
    left: 42px; top: 196px;
    font-family: "Playfair Display", serif; font-style: italic;
    font-size: 92px; letter-spacing: 4px;
    color: var(--steel-blue);
    text-shadow: -3px 3px 0 var(--sun-yellow);
  }
  .line--thirty {
    left: 392px; top: 210px;
    font-family: "Alfa Slab One", serif;
    font-size: 196px; letter-spacing: -6px;
    color: var(--slate);
    -webkit-text-stroke: 3px #f2f2f2;
  }
  .line--th {
    left: 744px; top: 244px;
    font-family: "Playfair Display", serif; font-style: italic;
    font-size: 48px; color: var(--slate);
  }
  .line--birthday {
    left: 42px; top: 336px;
    font-family: "Righteous", sans-serif;
    font-size: 76px;
    color: var(--sun-yellow);
    text-shadow: 4px 4px 0 var(--steel-blue);
  }
  .line--ampersand {
    left: 56px; top: 372px;
    font-family: "Playfair Display", serif; font-style: italic; font-weight: 700;
    font-size: 230px;
    color: var(--slate);
    text-shadow: -4px 4px 0 var(--sun-yellow);
  }
  .line--seventh {
    left: 272px; top: 414px;
    font-family: "Cormorant Garamond", serif; font-style: italic; font-weight: 500;
    font-size: 80px;
    color: var(--steel-blue);
  }
  .line--seventh sup { font-size: 0.5em; vertical-align: 0.8em; }
  .line--singapore {
    left: 196px; top: 478px;
    font-family: "Josefin Sans", sans-serif;
    font-size: 134px; letter-spacing: -2px;
    color: var(--slate);
    text-shadow: -5px 4px 0 var(--sun-yellow);
  }

  .skyline {
    position: absolute;
    left: 166px; top: 596px;
    width: 640px; height: 100px;
  }
  .portrait {
    position: absolute;
    left: 0; top: 470px;
    width: 500px; height: 658px;
  }

  .line--celebration {
    left: 362px; top: 692px;
    font-family: "Righteous", sans-serif;
    font-size: 70px; letter-spacing: 2px;
    color: var(--pale);
    -webkit-text-stroke: 3px var(--slate);
    text-shadow: 0 0 14px rgba(253,224,60,0.9);
  }
  .line--saturday {
    left: 452px; top: 770px;
    font-family: "Righteous", sans-serif;
    font-size: 70px;
    color: var(--steel-blue);
    text-shadow: -5px 4px 0 var(--sun-yellow);
  }
  .details {
    position: absolute;
    left: 524px; top: 836px;
    margin: 0; padding: 0; list-style: none;
    font-family: "Cormorant Garamond", serif; font-style: italic; font-weight: 500;
    font-size: 44px; line-height: 57px;
    color: var(--slate);
  }
</style>
</head>
<body>
<main class="invitation">
  <section class="invitation__panel">
    <h1 class="line line--you">YOU</h1>
    <p class="line line--are">are</p>
    <p class="line line--invited">invited</p>
    <p class="line line--to-my">to my</p>
    <p class="line line--thirty">30</p>
    <p class="line line--th">th</p>
    <p class="line line--birthday">Birthday</p>

    <svg class="portrait" viewBox="0 0 500 658" role="img" aria-label="Photo of the host in a red striped shirt holding a Singapore flag">
      <defs>
        <radialGradient id="portraitGlow" cx="35%" cy="55%" r="70%">
          <stop offset="0" stop-color="#f4a08f"/>
          <stop offset="0.55" stop-color="#f26a52" stop-opacity="0.85"/>
          <stop offset="1" stop-color="#e9ecec" stop-opacity="0"/>
        </radialGradient>
      </defs>
      <rect width="500" height="658" fill="url(#portraitGlow)"/>
    </svg>

    <p class="line line--ampersand">&amp;</p>
    <p class="line line--seventh">7<sup>th</sup> Year in</p>
    <p class="line line--singapore">singapore</p>

    <svg class="skyline" viewBox="0 0 640 100" role="img" aria-label="Line drawing of the Singapore skyline with its landmarks">
      <defs>
        <linearGradient id="skylineTone" x1="0" y1="0" x2="0" y2="1">
          <stop offset="0" stop-color="#c9cfd3" stop-opacity="0.3"/>
          <stop offset="1" stop-color="#b9bec2" stop-opacity="0.7"/>
        </linearGradient>
      </defs>
      <rect width="640" height="100" fill="url(#skylineTone)"/>
    </svg>

    <p class="line line--celebration">celebration</p>
    <p class="line line--saturday">saturday</p>
    <ul class="details">
      <li>june 29th</li>
      <li>8:30pm</li>
      <li>venu:</li>
    </ul>
  </section>
</main>
</body>
</html>
```